Celebratory PNG Overlays for use on social media related to cryptocurrency project

We need a couple of Overlays to be used in social media sharing for people who achieve certain ranks among our team members.
Must Include our logo, the title DRL VANGUARD Peaks, congratulations and the different ETH Winnings (5 ETH, 50ETH, 500ETH and 1000ETH).
(we award physical coins to members who attain these ranks, example images are added, you can use these as inspiration but it is NOT mandatory only optional)
Please use the provided template in regards to the space were photo and name must go, similar example in use provided

Please check the files added

Font styles to use
Sans Serif
Decorative

Requirements
Must have
• Our logo, DRL Vanguard Peaks , Congratulations and the different ammounts.
Must have the 2 items on the template.
Nice to have
• we award physical coins to members who attain these ranks, example images are added, you can use these as inspiration but it is NOT mandatory only optional)

```html
<!DOCTYPE html>
<html lang="en">
<head>
<meta charset="utf-8">
<title>DRL Vanguard Peaks – 5 ETH Overlay</title>
<link rel="stylesheet" href="https://fonts.googleapis.com/css2?family=Audiowide&family=Exo+2:ital,wght@1,800&display=swap">
<style>
  :root {
    --ink-dark: #161616;
    --ink-mid: #262626;
    --title-green: #3fe04a;
    --title-magenta: #e83bd0;
    --ring-orange: #f28a00;
    --ring-yellow: #ffe600;
    --photo-white: #ffffff;
    --plate-grey: #e8e8e8;
    --plate-green: #5fbf7a;
    --plate-red: #c8323a;
    --band-purple: #4a1f5a;
    --band-teal: #16d2d0;
    --diamond-blue: #2aa9cf;
    --diamond-light: #47bfe0;
    --text-white: #ffffff;
    --logo-gold: #d9b44a;
    --pattern-blue: #3b6fd8;
    --pattern-violet: #a05ad0;
    --pattern-red: #7a1e24;
  }
  html, body {
    margin: 0;
    padding: 0;
    width: 1127px;
    height: 1200px;
    overflow: hidden;
    background: var(--ink-dark);
  }
  .overlay {
    display: block;
    width: 1127px;
    height: 1200px;
  }
  .title {
    font-family: "Audiowide", sans-serif;
    font-size: 90px;
  }
  .title-green { fill: var(--title-green); }
  .title-magenta { fill: var(--title-magenta); }
  .congrats {
    font-family: "Audiowide", sans-serif;
    font-size: 68px;
    fill: var(--text-white);
  }
  .amount {
    font-family: "Exo 2", sans-serif;
    font-style: italic;
    font-weight: 800;
    fill: var(--text-white);
  }
  .amount-number { font-size: 140px; }
  .amount-unit { font-size: 58px; }
  .brand-name {
    font-family: "Audiowide", sans-serif;
    font-size: 68px;
    fill: var(--logo-gold);
  }
</style>
</head>
<body>
<svg class="overlay" viewBox="0 0 1127 1200" xmlns="http://www.w3.org/2000/svg">
  <defs>
    <linearGradient id="pattern-tone" x1="0" y1="0" x2="1" y2="1">
      <stop offset="0" stop-color="var(--pattern-blue)"/>
      <stop offset="0.55" stop-color="var(--pattern-violet)"/>
      <stop offset="1" stop-color="#e9d6f2"/>
    </linearGradient>
    <linearGradient id="left-tone" x1="0" y1="0" x2="0.6" y2="1">
      <stop offset="0" stop-color="#0f2a24"/>
      <stop offset="0.6" stop-color="#1c1c1c"/>
      <stop offset="1" stop-color="var(--pattern-red)"/>
    </linearGradient>
    <linearGradient id="ring-tone" x1="0" y1="0" x2="0" y2="1">
      <stop offset="0" stop-color="var(--ring-orange)"/>
      <stop offset="0.5" stop-color="var(--ring-yellow)"/>
      <stop offset="1" stop-color="var(--ring-orange)"/>
    </linearGradient>
    <linearGradient id="band-tone" x1="0" y1="0" x2="1" y2="0">
      <stop offset="0" stop-color="var(--band-purple)"/>
      <stop offset="0.55" stop-color="#2a6c8a"/>
      <stop offset="1" stop-color="var(--band-teal)"/>
    </linearGradient>
    <radialGradient id="coin-tone">
      <stop offset="0" stop-color="#f7e7b0"/>
      <stop offset="1" stop-color="#c79a3a"/>
    </radialGradient>
  </defs>

  <!-- background -->
  <rect class="bg-base" width="1127" height="1200" fill="var(--ink-dark)"/>
  <path class="bg-left" role="img" aria-label="Dark curved architectural backdrop"
        d="M0 0 H560 Q380 400 560 900 H0 Z" fill="url(#left-tone)"/>
  <path class="bg-right" role="img" aria-label="Flowing blue and violet mesh backdrop"
        d="M560 0 H1127 V900 H560 Q380 400 560 0 Z" fill="url(#pattern-tone)"/>

  <!-- title -->
  <text class="title" x="565" y="120" text-anchor="middle" textLength="1080" lengthAdjust="spacingAndGlyphs"><tspan class="title-green">DRL VANGUARD </tspan><tspan class="title-magenta">PEAKS</tspan></text>

  <!-- coins -->
  <circle class="coin coin-small" role="img" aria-label="Award coin" cx="124" cy="321" r="63" fill="url(#coin-tone)" opacity="0.75"/>
  <circle class="coin coin-faint" role="img" aria-label="Award coin" cx="972" cy="451" r="63" fill="#ffffff" opacity="0.18"/>

  <!-- photo frame -->
  <circle class="photo-ring" cx="538" cy="422" r="270" fill="url(#ring-tone)"/>
  <circle class="photo-shadow" cx="552" cy="425" r="250" fill="#0e3a3a"/>
  <circle class="photo-area" cx="560" cy="425" r="240" fill="var(--photo-white)"/>

  <!-- name plate -->
  <polygon class="plate-red" points="840,700 920,692 920,825 840,825" fill="var(--plate-red)"/>
  <polygon class="plate-green" points="205,702 988,640 988,700 205,730" fill="var(--plate-green)"/>
  <circle class="coin coin-large" role="img" aria-label="Award coin" cx="993" cy="812" r="125" fill="url(#coin-tone)" opacity="0.9"/>
  <polygon class="name-plate" points="131,716 916,652 916,815 131,815" fill="var(--plate-grey)"/>

  <!-- lower band -->
  <path class="lower-dark" d="M0 1200 V900 Q300 830 640 870 Q900 900 1127 880 V1200 Z" fill="var(--ink-mid)"/>
  <path class="congrats-band" d="M0 830 Q320 800 700 870 L760 970 Q420 940 0 1000 Z" fill="url(#band-tone)"/>
  <path class="band-edge" d="M0 1010 Q300 960 650 990" stroke="#c9893a" stroke-width="6" fill="none"/>

  <text class="congrats" x="393" y="902" text-anchor="middle" textLength="736" lengthAdjust="spacingAndGlyphs">CONGRATULATIONS</text>
  <text class="congrats" x="465" y="965" text-anchor="middle" textLength="352" lengthAdjust="spacingAndGlyphs">YOU WON</text>

  <!-- amount -->
  <polygon class="amount-diamond" points="606,1008 845,860 1085,1008 845,1155" fill="var(--diamond-blue)"/>
  <polygon class="unit-diamond" points="860,1120 986,1028 1127,1120 986,1200" fill="var(--diamond-light)"/>
  <text class="amount amount-number" x="855" y="1057" text-anchor="middle">5</text>
  <text class="amount amount-unit" x="1000" y="1138" text-anchor="middle">ETH</text>

  <!-- brand -->
  <circle class="brand-mark" cx="148" cy="1110" r="56" fill="var(--logo-gold)"/>
  <text class="brand-name" x="226" y="1134" textLength="500" lengthAdjust="spacingAndGlyphs">DRL VANGUARD</text>
</svg>
</body>
</html>
```